New lease of life for a tired Country Pub menu, QLD

I need to refresh my menus with updated prices. The menus need to be A4 (the menus are laminated and handed out over the bar. I'd like to include our logo. I will upload our existing menus as well as the new prices. The design should be humble yet stylish if that's ok, please

Target Market(s)

Locals, travellers and workers

Industry/Entity Type

Hospitality, Quintessential Country pub

Font styles to use
Sans Serif

Colors

Designer to choose colors to be used in the design.

Requirements
Must have
• as we run different menus on different nights
Nice to have
• our logo

```html
<!DOCTYPE html>
<html lang="en">
<head>
<meta charset="utf-8">
<title>Hotel Brennans – Lunch &amp; Pizza Menus</title>
<link href="https://fonts.googleapis.com/css2?family=Cormorant+Garamond:wght@500;600&family=Mulish:ital,wght@0,400;0,600;0,800;1,400&display=swap" rel="stylesheet">
<style>
  :root {
    --backdrop: #545554;
    --pattern: #efe3c6;
    --gold: #b07a3e;
    --line: #d2b06a;
    --ink: #6a6a6a;
    --ink-dark: #4a4a4a;
    --paper: #ffffff;
  }
  * { box-sizing: border-box; margin: 0; padding: 0; }
  html, body { width: 1200px; height: 864px; overflow: hidden; background: var(--backdrop); }
  .canvas { position: relative; width: 1200px; height: 864px; }
  .menu-sheet {
    position: absolute; top: 32px; width: 566px; height: 800px;
    background: var(--pattern);
  }
  .menu-sheet--lunch { left: 24px; }
  .menu-sheet--pizza { left: 610px; }
  .border-pattern { position: absolute; inset: 0; }
  .sheet-panel {
    position: absolute; inset: 21px; background: var(--paper);
    outline: 1px solid var(--line); outline-offset: -4px;
    font-family: "Mulish", sans-serif; color: var(--ink);
  }
  .venue-name {
    position: absolute; left: 0; right: 0; top: 34px; text-align: center;
    font-family: "Mulish", sans-serif; font-weight: 800; font-size: 24px;
    letter-spacing: 1px; color: var(--ink-dark); line-height: 1;
  }
  .menu-title {
    position: absolute; left: 0; right: 0; top: 96px; text-align: center;
    font-family: "Cormorant Garamond", serif; font-weight: 600; font-size: 30px;
    letter-spacing: 7px; color: var(--gold); line-height: 1;
  }
  .menu-hours {
    position: absolute; left: 0; right: 0; top: 129px; text-align: center;
    font-size: 12px; color: var(--ink); display: flex; justify-content: center; align-items: center; gap: 8px;
  }
  .menu-hours svg { width: 14px; height: 12px; }
  .menu-note {
    position: absolute; left: 0; right: 0; top: 155px; text-align: center;
    font-style: italic; font-size: 10.5px; color: var(--ink);
  }
  .price-head, .price { position: absolute; font-size: 10px; color: var(--ink); }
  .price-head { top: 175px; }
  .menu-item { position: absolute; left: 30px; width: 300px; }
  .item-name {
    font-family: "Cormorant Garamond", serif; font-weight: 600; font-size: 13.5px;
    color: var(--gold); letter-spacing: 0.3px; line-height: 1.1;
  }
  .item-desc { font-style: italic; font-size: 9.6px; line-height: 1.2; margin-top: 2px; }
  .item-extras { font-style: italic; font-size: 9.6px; line-height: 1.2; margin-top: 10px; }
  .price-col { position: absolute; font-size: 10px; line-height: 1.2; }
</style>
</head>
<body>
<main class="canvas">

  <section class="menu-sheet menu-sheet--lunch">
    <div class="border-pattern" role="img" aria-label="Gold geometric art deco border pattern"></div>
    <div class="sheet-panel">
      <div class="venue-name">HOTEL BRENNANS</div>
      <h1 class="menu-title">LUNCH MENU</h1>
      <p class="menu-hours">
        <svg viewBox="0 0 14 12"><path d="M0 6h9M9 6l-4-4M9 6l-4 4M10 6l4-3v6z" stroke="#b07a3e" stroke-width="1.2" fill="#b07a3e"/></svg>
        Tuesday – Saturday 12-2pm
        <svg viewBox="0 0 14 12"><path d="M14 6H5M5 6l4-4M5 6l4 4M4 6L0 3v6z" stroke="#b07a3e" stroke-width="1.2" fill="#b07a3e"/></svg>
      </p>
      <p class="menu-note">All burgers and wraps served with a side of chips</p>
      <span class="price-head" style="left:352px">Non-Members</span>
      <span class="price-head" style="left:446px">Members</span>

      <div class="menu-item" style="top:189px"><h2 class="item-name">CHICKEN BURGER</h2><p class="item-desc">Fried Harlow's Butchery crumbed chicken thigh, cheese,<br>tomato, spanish onion with aioli</p></div>
      <span class="price-col" style="left:352px;top:190px">$19.90</span><span class="price-col" style="left:446px;top:190px">$17.00</span>

      <div class="menu-item" style="top:252px"><h2 class="item-name">BEEF BURGER</h2><p class="item-desc">Grilled angus beef patty, lettuce, cheese, beetroot,<br>tomato, spanish onion, pickles, caramelised onion with aioli</p></div>
      <span class="price-col" style="left:352px;top:253px">$19.90</span><span class="price-col" style="left:446px;top:253px">$17.00</span>

      <div class="menu-item" style="top:316px"><h2 class="item-name">STEAK BURGER</h2><p class="item-desc">Grilled Harlow's Butchery rib fillet, lettuce, tomato, spanish<br>onion, beetroot, cheese, caramelised onion with bbq sauce</p></div>
      <span class="price-col" style="left:352px;top:317px">$21.00</span><span class="price-col" style="left:446px;top:317px">$19.00</span>

      <div class="menu-item" style="top:379px"><h2 class="item-name">BARRAMUNDI BURGER</h2><p class="item-desc">Southern fried barramundi, lettuce, coleslaw with<br>homemade dill and chives aioli</p></div>
      <span class="price-col" style="left:352px;top:380px">$18.99</span><span class="price-col" style="left:446px;top:380px">$17.00</span>

      <div class="menu-item" style="top:443px"><h2 class="item-name">CAESAR SALAD</h2><p class="item-desc">Cos lettuce, croutons, parmesan cheese, boiled egg,<br>caesar dressing</p>
        <p class="item-extras">ADD CHICKEN<br>ADD CALAMARI<br>WRAP IT – Chicken caesar salad wrap</p></div>
      <span class="price-col" style="left:352px;top:444px">$17.99</span><span class="price-col" style="left:446px;top:444px">$16.00</span>
      <span class="price-col" style="left:352px;top:490px">$21.00<br>$22.50<br>$19.00</span><span class="price-col" style="left:446px;top:490px">$19.00<br>$21.00<br>$16.00</span>

      <div class="menu-item" style="top:552px"><h2 class="item-name">HONEY MUSTARD CHICKEN SALAD</h2><p class="item-desc">Mesclun mix, continental cucumber, cherry tomato,<br>spanish onion, crispy chicken tenders (breast)</p></div>
      <span class="price-col" style="left:352px;top:553px">$19.00</span><span class="price-col" style="left:446px;top:553px">$17.00</span>

      <div class="menu-item" style="top:615px"><h2 class="item-name">BANGIN’ BEEF BURRITO</h2><p class="item-desc">Minced beef, sliced beef sausage, rice, tomato puree, herbs</p></div>
      <span class="price-col" style="left:352px;top:617px">$21.00</span><span class="price-col" style="left:446px;top:617px">$18.00</span>
    </div>
  </section>

  <section class="menu-sheet menu-sheet--pizza">
    <div class="border-pattern" role="img" aria-label="Gold geometric art deco border pattern"></div>
    <div class="sheet-panel">
      <div class="venue-name">HOTEL BRENNANS</div>
      <h1 class="menu-title">PIZZA MENU</h1>
      <p class="menu-hours">
        <svg viewBox="0 0 14 12"><path d="M0 6h9M9 6l-4-4M9 6l-4 4M10 6l4-3v6z" stroke="#b07a3e" stroke-width="1.2" fill="#b07a3e"/></svg>
        Lunch &amp; Dinner &nbsp;| &nbsp;Wednesdays Only
        <svg viewBox="0 0 14 12"><path d="M14 6H5M5 6l4-4M5 6l4 4M4 6L0 3v6z" stroke="#b07a3e" stroke-width="1.2" fill="#b07a3e"/></svg>
      </p>
      <p class="menu-note">HALF/ HALF NOT AVAILABLE</p>
      <span class="price-head" style="left:354px">Non-Members</span>
      <span class="price-head" style="left:456px">Members</span>

      <div class="menu-item" style="top:189px"><h2 class="item-name">HAWAIIAN</h2><p class="item-desc">Tomato sauce, cheddar cheese, Harlow's<br>smoked ham and pineapple, mozzarella</p></div>
      <span class="price-col" style="left:354px;top:190px">$24.50</span><span class="price-col" style="left:456px;top:190px">$22.00</span>

      <div class="menu-item" style="top:256px"><h2 class="item-name">MEATLOVER’S</h2><p class="item-desc">BBQ sauce, cheddar cheese, seasoned mince,<br>Harlow's smoked ham, beef sausage, mozzarella</p></div>
      <span class="price-col" style="left:354px;top:257px">$25.99</span><span class="price-col" style="left:456px;top:257px">$23.00</span>

      <div class="menu-item" style="top:323px"><h2 class="item-name">BBQ SWEET CHILLI CHICKEN</h2><p class="item-desc">BBQ sauce with sweet chili sauce, cheddar cheese,<br>mushrooms, onion, chicken, mozzarella</p></div>
      <span class="price-col" style="left:354px;top:324px">$24.50</span><span class="price-col" style="left:456px;top:324px">$22.00</span>

      <div class="menu-item" style="top:390px"><h2 class="item-name">SUPREME</h2><p class="item-desc">Tomato sauce, cheddar cheese, Harlow's smoked<br>ham, onion, capsicum, mushroom, pepperoni,<br>pineapple, mozzarella olives</p></div>
      <span class="price-col" style="left:354px;top:392px">$25.99</span><span class="price-col" style="left:456px;top:392px">$23.00</span>

      <div class="menu-item" style="top:472px"><h2 class="item-name">VEGETARIAN</h2><p class="item-desc">Tomato sauce, cheddar cheese, onion,<br>mushroom, capsicum, olives, pumpkin</p></div>
      <span class="price-col" style="left:354px;top:473px">$24.50</span><span class="price-col" style="left:456px;top:473px">$22.00</span>

      <div class="menu-item" style="top:539px"><h2 class="item-name">PEPPERONI</h2><p class="item-desc">Tomato sauce, cheddar cheese, pepperoni</p></div>
      <span class="price-col" style="left:354px;top:541px">$24.50</span><span class="price-col" style="left:456px;top:541px">$22.00</span>

      <div class="menu-item" style="top:595px"><h2 class="item-name">TANDOORI CHICKEN</h2><p class="item-desc">Tomato/tandoori sauce, cheddar cheese,<br>chicken, onion, capsicum, mozzarella</p></div>
      <span class="price-col" style="left:354px;top:596px">$24.50</span><span class="price-col" style="left:456px;top:596px">$22.00</span>
    </div>
  </section>

</main>
</body>
</html>
```